New therapy private practice needs a 2 sided postcard announcing location and services

We need a postcard sized card that is TWO SIDED and shares our new location and services offered. (new location is 3842. W. 58th #2300 in Tulsa, OK 74152) Name of the therapy business is "Bright Path! Counseling". Services offered include individual, marriage, family and group counseling. My phone number to place on the card is (918) 555-0143 and someone can call to schedule a free 20 minute consultation at that number.

These cards will also be mailed in an enclosed envelope or placed in welcome baskets as a marketing tool with possible referral sources like churches, doctors, and lawyers. (That means there does not have to be a space for an address or stamp to mail to. Full use of both sides of the card is important) We would like to see designs that use softer colors such as blue, purples, or greens. The final design should communicate a feeling of peace and hope and a sense of freshness and approachability. Incorporating a tag line such as..... "where you'll find hope!" would be good. My website is www.brightpathnow.example and extra info about my practice is on there. It is important my credentials are listed on the postcard. Lena Marsh Voight, LPC-S, LMFT

I am not looking for a bunch of "box looking pictures". The pictures I am uploading are for ideas, although my logo and picture should be used. I like the type of picture I have on my homepage of my website with the quote "Let your hopes, not your fears shape your future"

Target Market(s)

Primarily women and couples looking for counseling for relationships, anxiety, depression, or life transitions.

Font styles to use
Serif
Script

Colors
3276b5
85acd3
86cfc6
33b8a4
cadf82
876aae
9bcb3c

Requirements
Must have
• My picture, address, website, and phone number as well as my logo.
• Address is: 3842 W. 58th Street #2300 Tulsa, OK 74152
• Web: www.brightpathnow.example
• Email: lena@brightpathnow.example
• Phone: (918) 555-0143
• "Hope anchors the soul" - Heb. 6:19
• On my website, I have a 2 minute video of myself. This may be helpful to watch in getting a "feel" for my counseling practice.
• Services Provided: ANXIETY | DEPRESSION | LIFE TRANSITIONS | MARRIAGE COUNSELING | SEPARATION AND DIVORCE | WOMEN’S ISSUES | ADDICTIONS AND INFIDELITY | PARENT/CHILD RELATIONSHIPS | FAMILY CONFLICT | TRAUMA/GRIEF AND LOSS
Nice to have
• A combination of print and script would be nice. A feeling of tranquility and hope
• I would like to have the statement at the bottom of the card.... " It is my desire for you to discover that no matter the situation you are currently going through….. there’s hope!"
• It would also be nice to have a small area that says: Lena is a graduate of Western Calloway College and has been in private practice for 11 years. She is a regular monthly co-host on the Meadow Broadcast Group at 97.3 FM
Should not have
• Heavy bold or abrasive feel

```html
<!DOCTYPE html>
<html lang="en">
<head>
<meta charset="utf-8">
<title>Bright Path! Counseling – Postcard</title>
<link rel="stylesheet" href="https://fonts.googleapis.com/css2?family=Lato:ital,wght@0,400;0,700;0,900;1,700&display=swap">
<style>
  :root{
    --page:#e8e5e1;
    --card-light:#e4e6ea;
    --card-lighter:#f1f1f2;
    --forest-dark:#2b2a20;
    --forest-mid:#5a5236;
    --forest-light:#9a8a5e;
    --green:#5cb531;
    --silver:#9a9da2;
    --ink:#2a2a2a;
    --ink-soft:#3d3d3d;
    --logo-green:#4f9a2e;
    --bio-blue:#4aa8c9;
    --white:#ffffff;
    --room-warm:#ebe6df;
    --room-cool:#f6f5f3;
  }
  *{box-sizing:border-box;margin:0;padding:0}
  html,body{width:902px;height:1200px;overflow:hidden}
  body{background:var(--page);font-family:"Lato",Arial,sans-serif;color:var(--ink);position:relative}

  .card{position:absolute;width:710px;height:477px;overflow:hidden;box-shadow:0 4px 14px rgba(0,0,0,.25)}
  .card--front{left:48px;top:116px;background:var(--card-light)}
  .card--back{left:123px;top:646px;background:var(--card-lighter)}

  .photo{position:absolute}
  .photo--landscape{left:0;top:0;width:710px;height:320px;
    background:radial-gradient(ellipse at 30% 0%,#c9b98d 0%,transparent 45%),
               linear-gradient(180deg,var(--forest-light) 0%,var(--forest-mid) 35%,var(--forest-dark) 100%)}
  .photo--room{left:0;top:0;width:710px;height:477px;
    background:linear-gradient(180deg,var(--room-cool) 0%,var(--room-warm) 70%,#d9d2c6 100%)}
  .photo--portrait{left:0;bottom:0;width:245px;height:255px;
    background:radial-gradient(ellipse at 50% 35%,#d8b48c 0%,#b28a5a 35%,#6e3144 75%,#3a2b3c 100%)}
  .card--back .photo--portrait{left:62px;width:245px;height:240px}

  .wave{position:absolute;left:0;top:0;width:710px;height:477px}

  .headline{position:absolute;left:52px;top:56px;color:var(--white);font-size:40px;line-height:50px;font-weight:400;text-shadow:0 1px 4px rgba(0,0,0,.35)}
  .headline strong{font-weight:700}

  .logo{position:absolute;display:flex;align-items:center;gap:9px;color:var(--logo-green);font-weight:700;line-height:1.15}
  .logo__dot{width:26px;height:26px;border-radius:50%;background:var(--logo-green);flex:none}
  .card--front .logo{left:488px;top:336px;font-size:21px}
  .card--back .logo{left:82px;top:48px;font-size:19px;white-space:nowrap}

  .ident{position:absolute;left:274px;top:414px}
  .ident__name{font-size:20px;font-weight:700;color:var(--ink)}
  .ident__creds{font-size:15px;font-weight:700;color:var(--ink-soft);margin-top:2px}
  .ident__rule{position:absolute;left:460px;top:420px;width:1px;height:44px;background:var(--silver)}
  .ident__phone{position:absolute;left:477px;top:416px;font-size:27px;font-weight:700;color:var(--ink-soft)}
  .ident__offer{position:absolute;left:478px;top:451px;font-size:12px;font-weight:400;color:var(--ink-soft);white-space:nowrap}

  .contact{position:absolute;left:62px;top:143px;list-style:none}
  .contact li{display:flex;align-items:center;gap:11px;font-size:14.5px;color:var(--ink);height:21px;white-space:nowrap}
  .contact svg{width:14px;height:14px;flex:none}

  .services{position:absolute;left:413px;top:22px}
  .services__title{font-size:17px;font-weight:400;letter-spacing:.3px;color:var(--ink);margin-bottom:5px}
  .services__list{list-style:none}
  .services__list li{display:flex;align-items:center;gap:14px;font-size:11.5px;height:19.6px;color:var(--ink-soft);text-transform:uppercase}
  .services__list svg{width:13px;height:13px;flex:none}

  .quote{position:absolute;left:378px;top:306px;width:330px;font-style:italic;font-weight:700;font-size:14px;line-height:19px;color:var(--ink)}
  .bio{position:absolute;left:376px;top:366px;width:334px;height:77px;background:var(--bio-blue);color:var(--white);font-size:10.6px;font-weight:700;line-height:13px;padding:5px 8px}
  .verse{position:absolute;right:34px;top:450px;font-size:11.5px;color:var(--ink-soft)}
</style>
</head>
<body>

<section class="card card--front" aria-label="Postcard front">
  <div class="photo photo--landscape" role="img" aria-label="Photo of a person sitting on a rock overlooking a misty forest valley at sunrise"></div>
  <svg class="wave" viewBox="0 0 710 477" preserveAspectRatio="none" aria-hidden="true">
    <path d="M0,340 C180,330 360,250 710,268 L710,290 C380,270 200,340 0,350 Z" fill="var(--silver)"/>
    <path d="M0,328 C200,318 380,252 710,272 L710,292 C390,276 200,345 0,350 Z" fill="var(--green)"/>
    <path d="M0,350 C200,345 390,276 710,292 L710,477 L0,477 Z" fill="var(--card-light)"/>
  </svg>
  <h1 class="headline"><strong>Let your Hopes,</strong><br>not your hurts,<br>shape your future.</h1>
  <div class="photo photo--portrait" role="img" aria-label="Portrait photo of the counselor smiling outdoors"></div>
  <div class="logo"><span class="logo__dot"></span><span>Bright Path!<br>Counseling</span></div>
  <div class="ident">
    <div class="ident__name">Lena Marsh Voight</div>
    <div class="ident__creds">LPC-S, LMFT</div>
  </div>
  <div class="ident__rule"></div>
  <div class="ident__phone">(918) 555-0143</div>
  <div class="ident__offer">Call for a free 20 minute consultation</div>
</section>

<section class="card card--back" aria-label="Postcard back">
  <div class="photo photo--room" role="img" aria-label="Photo of a bright, calm counseling office with a sofa and lamp"></div>
  <div class="logo"><span class="logo__dot"></span>Bright Path! Counseling</div>

  <ul class="contact">
    <li><svg viewBox="0 0 16 16"><circle cx="8" cy="8" r="7" fill="none" stroke="#2a2a2a" stroke-width="1.3"/><path d="M5.5 4.5l1.5 1.6-.8 1.1a5 5 0 002.6 2.6l1.1-.8 1.6 1.5-.9 1.1c-2.8-.3-5.2-2.7-5.5-5.5z" fill="#2a2a2a"/></svg>(918) 555-0143</li>
    <li><svg viewBox="0 0 16 16" fill="none" stroke="#2a2a2a" stroke-width="1.3"><circle cx="8" cy="8" r="7"/><ellipse cx="8" cy="8" rx="3" ry="7"/><path d="M1 8h14M2.5 4.5h11M2.5 11.5h11"/></svg>www.brightpathnow.example</li>
    <li><svg viewBox="0 0 16 16"><path d="M1 3h14v10H1z" fill="#2a2a2a"/><path d="M1 3l7 5 7-5" fill="none" stroke="#fff" stroke-width="1.2"/></svg>lena@brightpathnow.example</li>
    <li><svg viewBox="0 0 16 16"><path d="M8 1a4 4 0 014 4c0 3-4 7-4 7S4 8 4 5a4 4 0 014-4z" fill="#2a2a2a"/><circle cx="8" cy="5" r="1.5" fill="#fff"/><ellipse cx="8" cy="14" rx="5" ry="1.4" fill="#2a2a2a"/></svg>3842 W. 58th Street #2300 Tulsa, OK 74152</li>
  </ul>

  <div class="services">
    <h2 class="services__title">SERVICES PROVIDED :</h2>
    <ul class="services__list">
      <li><svg viewBox="0 0 14 14" fill="none" stroke="#2a2a2a" stroke-width="1.3"><circle cx="7" cy="7" r="6"/><path d="M4 7l2.3 2.5L13 1"/></svg>Anxiety</li>
      <li><svg viewBox="0 0 14 14" fill="none" stroke="#2a2a2a" stroke-width="1.3"><circle cx="7" cy="7" r="6"/><path d="M4 7l2.3 2.5L13 1"/></svg>Depression</li>
      <li><svg viewBox="0 0 14 14" fill="none" stroke="#2a2a2a" stroke-width="1.3"><circle cx="7" cy="7" r="6"/><path d="M4 7l2.3 2.5L13 1"/></svg>Life Transitions</li>
      <li><svg viewBox="0 0 14 14" fill="none" stroke="#2a2a2a" stroke-width="1.3"><circle cx="7" cy="7" r="6"/><path d="M4 7l2.3 2.5L13 1"/></svg>Marriage Counseling</li>
      <li><svg viewBox="0 0 14 14" fill="none" stroke="#2a2a2a" stroke-width="1.3"><circle cx="7" cy="7" r="6"/><path d="M4 7l2.3 2.5L13 1"/></svg>Separation and Divorce</li>
      <li><svg viewBox="0 0 14 14" fill="none" stroke="#2a2a2a" stroke-width="1.3"><circle cx="7" cy="7" r="6"/><path d="M4 7l2.3 2.5L13 1"/></svg>Women's Issues</li>
      <li><svg viewBox="0 0 14 14" fill="none" stroke="#2a2a2a" stroke-width="1.3"><circle cx="7" cy="7" r="6"/><path d="M4 7l2.3 2.5L13 1"/></svg>Addictions and Infidelity</li>
      <li><svg viewBox="0 0 14 14" fill="none" stroke="#2a2a2a" stroke-width="1.3"><circle cx="7" cy="7" r="6"/><path d="M4 7l2.3 2.5L13 1"/></svg>Parent/Child Relationships</li>
      <li><svg viewBox="0 0 14 14" fill="none" stroke="#2a2a2a" stroke-width="1.3"><circle cx="7" cy="7" r="6"/><path d="M4 7l2.3 2.5L13 1"/></svg>Family Conflict</li>
      <li><svg viewBox="0 0 14 14" fill="none" stroke="#2a2a2a" stroke-width="1.3"><circle cx="7" cy="7" r="6"/><path d="M4 7l2.3 2.5L13 1"/></svg>Trauma/Grief and Loss</li>
    </ul>
  </div>

  <svg class="wave" viewBox="0 0 710 477" preserveAspectRatio="none" aria-hidden="true">
    <path d="M0,243 C150,300 420,240 710,275 L710,290 C420,258 160,318 0,262 Z" fill="var(--silver)"/>
    <path d="M0,236 C150,292 420,232 710,265 L710,285 C420,254 160,314 0,262 Z" fill="var(--green)"/>
    <path d="M0,262 C160,314 420,254 710,285 L710,477 L0,477 Z" fill="var(--card-lighter)"/>
  </svg>

  <div class="photo photo--portrait" role="img" aria-label="Portrait photo of the counselor smiling outdoors"></div>

  <p class="quote">“It is my desire for you to discover that no matter<br>the situation you are currently going through…..<br>there’s hope!”</p>
  <p class="bio">Lena Marsh Voight is a Licensed Professional Counselor and a Licensed Marriage and Family Therapist. She is a graduate of Western Calloway College and has been in private practice since 2007. Lena is a regular guest co-host on the Meadow Broadcast Group KMBG at 97.3 FM</p>
  <p class="verse">Hope anchors the soul - Heb. 6:19</p>
</section>

</body>
</html>
```